M&A Advisory firm needs elegant and powerful letterhead

We need a powerful but elegant letterhead to engage with the international financial industry.

Target Market(s)

New York and International Financial Industry

Industry/Entity Type

Finance

Font styles to use
Other font styles liked:
• Poppins

Requirements
Must have
• 482 W 71st Street 14th Floor New York, NY 10157 O: +1 (212) 555 0147 F: +1 (212) 555 0182

```html
<!DOCTYPE html>
<html lang="en">
<head>
<meta charset="utf-8">
<title>Halvern Letterhead</title>
<link rel="stylesheet" href="https://fonts.googleapis.com/css2?family=Poppins:wght@400;500;600&display=swap">
<style>
  :root {
    --backdrop: #d9cbb2;
    --paper: #ffffff;
    --brand-blue: #0b4f93;
    --band-grey: #b3b3b5;
    --text-dark: #2b2b2b;
    --text-muted: #7a7a7a;
  }
  * { box-sizing: border-box; margin: 0; padding: 0; }
  html, body {
    width: 1200px;
    height: 898px;
    overflow: hidden;
    background: var(--backdrop);
    font-family: "Poppins", sans-serif;
  }
  .letterhead {
    position: absolute;
    left: 296px;
    top: 19px;
    width: 608px;
    height: 860px;
    background: var(--paper);
    box-shadow: 0 6px 20px rgba(0,0,0,0.12);
    overflow: hidden;
  }
  .letterhead__bands {
    position: absolute;
    inset: 0;
    width: 100%;
    height: 100%;
  }
  .band--grey { fill: var(--band-grey); }
  .band--blue { fill: var(--brand-blue); }

  .brand {
    position: absolute;
    left: 56px;
    top: 92px;
    display: flex;
    align-items: center;
    gap: 12px;
  }
  .brand__dot {
    width: 26px;
    height: 26px;
    border-radius: 50%;
    background: var(--brand-blue);
  }
  .brand__name {
    font-size: 34px;
    font-weight: 400;
    letter-spacing: 1px;
    color: var(--brand-blue);
    line-height: 1;
  }

  .letter-body {
    position: absolute;
    left: 70px;
    top: 230px;
    width: 440px;
    color: var(--text-dark);
  }
  .letter-body__heading {
    font-size: 12px;
    font-weight: 600;
    margin-bottom: 18px;
  }
  .letter-body__para {
    font-size: 8.4px;
    line-height: 2.05;
    text-align: justify;
    margin-bottom: 22px;
  }

  .contact {
    position: absolute;
    right: 60px;
    top: 640px;
    font-size: 9px;
    line-height: 1.75;
    color: var(--text-muted);
  }
  .contact__row { display: flex; gap: 4px; }
  .contact__label {
    font-weight: 600;
    color: var(--brand-blue);
    width: 12px;
  }
</style>
</head>
<body>
  <main class="letterhead">
    <svg class="letterhead__bands" viewBox="0 0 608 860" preserveAspectRatio="none" aria-hidden="true">
      <polygon class="band--grey" points="190,0 608,0 608,48 190,6"/>
      <polygon class="band--blue" points="300,0 608,0 608,6 408,60"/>
      <polygon class="band--grey" points="0,752 330,730 0,822"/>
      <polygon class="band--blue" points="0,860 0,836 330,728 530,726 230,860"/>
    </svg>

    <header class="brand">
      <span class="brand__dot"></span>
      <span class="brand__name">HALVERN</span>
    </header>

    <section class="letter-body">
      <h1 class="letter-body__heading">Lorem ipsum</h1>
      <p class="letter-body__para">Lorem ipsum dolor sit amet, consectetuer adipiscing elit, sed diam nonummy nibh euismod tincidunt ut laoreet dolore magna aliquam erat volutpat. Ut wisi enim ad minim veniam, quis nostrud exerci tation ullamcorper suscipit lobortis nisl ut aliquip ex ea commodo consequat. Duis autem vel eum iriure dolor in hendrerit in vulputate velit esse molestie consequat, vel illum dolore eu feugiat nulla facilisis at vero eros et accumsan et iusto odio dignissim qui blandit praesent luptatum zzril delenit augue duis dolore te feugait nulla facilisi. Lorem ipsum dolor sit amet, cons ectetuer adipiscing elit, sed diam nonummy nibh euismod tincidunt ut laoreet dolore magna aliquam erat volutpat. Ut wisi enim ad minim veniam, quis nostrud exerci tation ullamcorper suscipit lobortis nisl ut aliquip ex ea commodo consequat.</p>
      <p class="letter-body__para">Lorem ipsum dolor sit amet, consectetuer adipiscing elit, sed diam nonummy nibh euismod tincidunt ut laoreet dolore magna aliquam erat volutpat. Ut wisi enim ad minim veniam, quis nostrud exerci tation ullamcorper suscipit lobortis nisl ut aliquip ex ea commodo consequat. Duis autem vel eum iriure dolor in hendrerit in vulputate velit esse molestie consequat, vel illum dolore eu feugiat nulla facilisis at vero eros et accumsan et iusto odio dignissim qui blandit praesent luptatum zzril delenit augue duis dolore te feugait nulla facilisi. Lorem ipsum dolor sit amet, cons ectetuer adipiscing elit, sed diam nonummy nibh euismod tincidunt ut laoreet dolore magna aliquam erat volutpat. Ut wisi enim ad minim veniam, quis nostrud exerci tation ullamcorper suscipit lobortis nisl ut aliquip ex ea commodo consequat.</p>
    </section>

    <address class="contact" style="font-style: normal;">
      <div class="contact__row"><span class="contact__label">A:</span><span>482 W 71st Street 14th Floor<br>New York, NY 10157</span></div>
      <div class="contact__row"><span class="contact__label">P:</span><span>+1 (212) 555 0147</span></div>
      <div class="contact__row"><span class="contact__label">F:</span><span>+1 (212) 555 0182</span></div>
    </address>
  </main>
</body>
</html>
```